Zielgruppe
Wir sind ein Team von SW Experten, die unterschiedliche SW Projekte unterstützen, kontinuierlich die Qualität der SW zu erhöhen durch schnelles Feedback bei Änderungen.
Unsere Zielgruppe sind SW Entwicklungsteams für embedded systems (automotive und none-automotive) (Software Entwickler, Software Architekten, Tester, Projektleiter, Qualitätssicherung)
Aufgabenstellung
Das zu bewerbende Projekt heißt KORVU - Kernel- and Module Orchestration via Rules Unit. Vision ist 'We support you to achieve your Project Goals'
Das Produkt führt automatisierte datenbasierte Analysen der SW Modelle und Implementierung durch, ist cloud basiert, einfach skalierbar und kann plug and play in die bestehende IT Infrastruktur eingebunden werden. Es gibt schnelle Rückmeldungen bei Änderungen und unterstützt die Teams dadurch qualitativ hochwertige Software zu entwickeln.
Grundfarbe unserer Präsentationen ist hex #429FB6
Wir haben vor ein 2m x 2m Canvas erstellen und ggf. DIN A0 Plakate.

```html
<!DOCTYPE html>
<html lang="en">
<head>
<meta charset="utf-8">
<title>KORVU – Kernel- and Module Orchestration via Rules Unit</title>
<link rel="stylesheet" href="https://fonts.googleapis.com/css2?family=Oswald:wght@400;500;600&display=swap">
<style>
  :root {
    --teal: #2a9eb6;
    --plum: #4a3658;
    --white: #ffffff;
    --ink: #0a0707;
    --shadow: #8a8a8a;
    --veil-strong: rgba(214, 230, 236, 0.88);
    --veil-soft: rgba(255, 255, 255, 0.45);
  }
  html, body {
    margin: 0;
    padding: 0;
    width: 1200px;
    height: 1200px;
    overflow: hidden;
    background: var(--teal);
  }
  .poster {
    display: block;
    width: 1200px;
    height: 1200px;
    background: var(--teal);
  }
  .veil-large { fill: var(--veil-strong); opacity: 0.85; }
  .veil-soft { fill: var(--veil-soft); }
  .tile { fill: var(--white); }
  .tile-shadow { fill: var(--shadow); }
  .ink { fill: var(--ink); }
  .ink-line { stroke: var(--ink); fill: none; }
  .paper { fill: var(--white); }
  .brand-name {
    font-family: "Oswald", sans-serif;
    font-weight: 600;
    font-size: 118px;
    fill: var(--plum);
    letter-spacing: 2px;
  }
  .vision {
    font-family: "Oswald", sans-serif;
    font-weight: 500;
    font-size: 33px;
    fill: var(--plum);
  }
  .product-title {
    font-family: "Oswald", sans-serif;
    font-weight: 400;
    font-size: 58px;
    fill: var(--plum);
  }
  .gear-body { fill: var(--white); }
  .gear-teeth { stroke: var(--white); fill: none; }
  .gear-shadow-body { fill: var(--shadow); }
  .gear-shadow-teeth { stroke: var(--shadow); fill: none; }
  .gear-hole { fill: var(--teal); }
  .person-area { fill: #1b1717; }
</style>
</head>
<body>
<svg class="poster" viewBox="0 0 1200 1200" width="1200" height="1200" xmlns="http://www.w3.org/2000/svg">

  <!-- translucent honeycomb backdrop -->
  <g class="honeycomb-backdrop">
    <polygon class="veil-large" points="129,384 582,156 1035,384 1035,894 582,1116 129,894"/>
    <polygon class="veil-soft" points="378,84 525,9 672,84 672,348 525,420 378,348"/>
    <polygon class="veil-soft" points="538,279 660,218 784,279 784,444 660,503 538,444"/>
    <polygon class="veil-soft" points="642,498 791,427 938,498 938,696 791,768 642,696"/>
    <polygon class="veil-soft" points="378,660 525,587 671,660 671,858 525,930 378,858"/>
    <polygon class="veil-soft" points="183,924 295,867 408,924 408,1071 295,1128 183,1071"/>
  </g>

  <!-- gear -->
  <g class="gear" transform="translate(944 222)">
    <g transform="translate(6 8)">
      <circle class="gear-shadow-body" r="98"/>
      <circle class="gear-shadow-teeth" r="108" stroke-width="26" stroke-dasharray="30 37.86"/>
    </g>
    <circle class="gear-body" r="98"/>
    <circle class="gear-teeth" r="108" stroke-width="26" stroke-dasharray="30 37.86"/>
    <circle class="gear-hole" r="24"/>
  </g>

  <!-- vision statement -->
  <g class="vision-block" transform="translate(642 147) rotate(26)">
    <text class="vision" x="0" y="0">We support you to achieve</text>
    <text class="vision" x="166" y="38">your Project Goals</text>
  </g>

  <!-- brand tile -->
  <g class="brand-tile">
    <polygon class="tile-shadow" points="72,279 297,167 521,279 521,576 297,687 72,576"/>
    <polygon class="tile" points="66,273 291,161 515,273 515,570 291,681 66,570"/>
    <text class="brand-name" x="291" y="462" text-anchor="middle">KORVU</text>
  </g>

  <!-- code window tile -->
  <g class="code-tile">
    <polygon class="tile-shadow" points="446,107 532,65 618,107 618,222 532,264 446,222"/>
    <polygon class="tile" points="441,102 527,60 613,102 613,217 527,259 441,217"/>
    <rect class="ink" x="457" y="105" width="141" height="109"/>
    <rect class="paper" x="468" y="133" width="120" height="71"/>
    <circle class="paper" cx="554" cy="119" r="3.2"/>
    <circle class="paper" cx="566" cy="119" r="3.2"/>
    <circle class="paper" cx="579" cy="119" r="3.2"/>
    <polyline class="ink-line" points="507,153 490,169 507,185" stroke-width="6"/>
    <polyline class="ink-line" points="547,153 564,169 547,185" stroke-width="6"/>
    <line class="ink-line" x1="533" y1="149" x2="521" y2="189" stroke-width="5"/>
  </g>

  <!-- developer illustration area -->
  <rect class="person-area" x="578" y="243" width="168" height="215" rx="18"
        role="img" aria-label="Illustration of a developer working at a laptop showing code brackets"/>

  <!-- radar chart tile -->
  <g class="radar-tile">
    <polygon class="tile-shadow" points="677,521 797,462 917,521 917,681 797,739 677,681"/>
    <polygon class="tile" points="671,515 791,456 911,515 911,675 791,733 671,675"/>
    <g class="ink-line" stroke-width="3.5">
      <line x1="792" y1="594" x2="792" y2="499"/>
      <line x1="792" y1="594" x2="693" y2="570"/>
      <line x1="792" y1="594" x2="889" y2="571"/>
      <line x1="792" y1="594" x2="729" y2="687"/>
      <line x1="792" y1="594" x2="853" y2="687"/>
      <polygon points="792,524 847,581 819,638 751,655 725,578"/>
    </g>
  </g>

  <!-- process flow tile -->
  <g class="flow-tile">
    <polygon class="tile-shadow" points="308,711 420,655 533,711 533,858 420,913 308,858"/>
    <polygon class="tile" points="302,705 414,649 527,705 527,852 414,907 302,852"/>
    <circle class="ink" cx="360" cy="718" r="23"/>
    <line class="ink-line" x1="393" y1="717" x2="434" y2="717" stroke-width="5"/>
    <polyline class="ink-line" points="425,708 435,717 425,726" stroke-width="5" stroke-linecap="round" stroke-linejoin="round"/>
    <polygon class="ink" points="469,693 494,718 469,743 444,718"/>
    <line class="ink-line" x1="469" y1="753" x2="469" y2="797" stroke-width="5"/>
    <polyline class="ink-line" points="460,788 469,798 478,788" stroke-width="5" stroke-linecap="round" stroke-linejoin="round"/>
    <circle class="ink" cx="469" cy="831" r="23"/>
    <line class="ink-line" x1="435" y1="831" x2="394" y2="831" stroke-width="5"/>
    <polyline class="ink-line" points="403,822 393,831 403,840" stroke-width="5" stroke-linecap="round" stroke-linejoin="round"/>
    <rect class="ink" x="337" y="808" width="46" height="46"/>
  </g>

  <!-- database icon -->
  <g class="database-icon">
    <rect class="ink" x="231" y="920" width="130" height="46" rx="6"/>
    <ellipse class="ink" cx="296" cy="920" rx="65" ry="14"/>
    <ellipse class="ink" cx="296" cy="966" rx="65" ry="14"/>
    <rect class="ink" x="231" y="978" width="130" height="46"/>
    <ellipse class="ink" cx="296" cy="1024" rx="65" ry="14"/>
    <rect class="ink" x="231" y="1036" width="130" height="40"/>
    <ellipse class="ink" cx="296" cy="1076" rx="65" ry="14"/>
    <path d="M231 968 Q296 990 361 968" stroke="#d6e6ec" stroke-width="4" fill="none"/>
    <path d="M231 1026 Q296 1048 361 1026" stroke="#d6e6ec" stroke-width="4" fill="none"/>
    <circle class="paper" cx="342" cy="953" r="4.5"/>
    <circle class="paper" cx="342" cy="1011" r="4.5"/>
    <circle class="paper" cx="342" cy="1068" r="4.5"/>
  </g>

  <!-- product title -->
  <g class="product-title-block" transform="translate(742 855) rotate(-28)">
    <text class="product-title" x="0" y="0" text-anchor="middle">KORVU - Kernel- and</text>
    <text class="product-title" x="0" y="78" text-anchor="middle">Module Orchestration</text>
    <text class="product-title" x="0" y="156" text-anchor="middle">via Rules Unit</text>
  </g>

</svg>
</body>
</html>
```